Veltrix inc. Aviation website

we are looking for a very modern and luxury web design, we are an aviation based company and specialize in aircraft exports and setup of air services world wide.
we want the website to be unique, creative, luxurious, professional, and to make an statement.
we have attached the logo.
our business cards theme is black background with gold stamping, if that is the rout you want to take.
**The format we are looking for is Wordpress.**
**the website is www.veltrixinc-example.com**
** 3 pages:
1. home page: -overview/about us
-industry leading
- worldwide presence
- aerial support
2. products and services: -business aircrafts
-commercial aircrafts
-amphibious aircrafts
-operation setup
-maintenance & crew training
3. contact us
**our location: Marlow Fenwick Harbour Airfield, Hangar 14**
we do appreciate suggestions
Thank you all.
Target Market(s)
Aviation professionals, Aircraft import/export, airlines, air taxi operations
Industry/Entity Type
It Company
Number of Pages Required
3 page
Requirements
Must have
- must have a very modern and luxurious design, and must be aviation oriented, and must have the logo, must be professional looking and be animated.
Nice to have
- black, gold, and burgandy colour
Should not have
- should not be playful and cartoony.

```html
<!DOCTYPE html>
<html lang="en">
<head>
<meta charset="utf-8">
<title>Veltrix inc. — Aviation</title>
<link href="https://fonts.googleapis.com/css2?family=Roboto:wght@300;400;500;700&family=Roboto+Condensed:wght@400;700&display=swap" rel="stylesheet">
<style>
:root{
  --black:#0b0b0b;
  --footer:#111111;
  --bar:#1a1a1a;
  --gold:#a27b1d;
  --gold-light:#b8912e;
  --burgundy:#7b1a1b;
  --grey-panel:#ececec;
  --text-dark:#3a3a3a;
  --text-muted:#6a6a6a;
  --footer-text:#8d8d8d;
  --white:#ffffff;
}
*{margin:0;padding:0;box-sizing:border-box}
html,body{width:755px;height:1200px;overflow:hidden;background:var(--black)}
body{position:relative;font-family:"Roboto",Arial,sans-serif;color:var(--white)}
.abs{position:absolute}

/* header */
.site-header{left:0;top:0;width:755px;height:49px;background:var(--black)}
.brand{left:63px;top:14px;display:flex;align-items:center;gap:8px;font-size:17px;font-weight:400;letter-spacing:2px;color:var(--gold-light)}
.brand-mark{width:14px;height:14px;background:var(--gold)}
.main-nav{left:328px;top:19px;display:flex;font-size:8px;letter-spacing:.2px}
.main-nav span{margin-right:40px}
.main-nav span:last-child{margin-right:0}

/* hero */
.hero{left:0;top:49px;width:755px;height:361px;
  background:radial-gradient(ellipse at 30% 20%,#e9b36a 0%,#c57b3f 35%,#7b4a34 70%,#4a3a3a 100%)}
.hero-photo{left:0;top:0;width:755px;height:361px;
  background:linear-gradient(160deg,rgba(255,220,170,.35) 0%,rgba(0,0,0,0) 45%,rgba(40,30,40,.45) 100%)}
.hero-title{left:61px;top:210px;font-size:40px;font-weight:300;letter-spacing:3px}
.hero-tagline{left:61px;top:260px;font-size:14px;font-weight:300;line-height:24px;letter-spacing:.2px}
.hero-dots{left:718px;top:190px;display:flex;flex-direction:column;gap:10px}
.hero-dots i{display:block;width:5px;height:5px;border-radius:50%;background:#e6e0da}
.hero-dots i:first-child{background:transparent;border:1px solid #e6e0da}
.scroll-down{left:365px;top:316px}

/* about row */
.about-photo{left:0;top:410px;width:214px;height:306px;background:linear-gradient(150deg,#3a4150 0%,#6d7686 50%,#d9dde3 100%)}
.about-panel{left:214px;top:410px;width:297px;height:306px;background:var(--grey-panel)}
.about-kicker{left:256px;top:456px;font-size:21px;font-weight:400;color:var(--text-dark)}
.about-title{left:256px;top:480px;font-size:29px;font-weight:700;font-family:"Roboto Condensed","Roboto",sans-serif;color:var(--gold);letter-spacing:.5px}
.about-copy{left:258px;top:521px;width:220px;font-size:7.3px;line-height:15.6px;color:var(--text-muted)}
.about-copy p+p{margin-top:15.6px}
.support-photo{left:511px;top:410px;width:244px;height:143px;background:linear-gradient(120deg,#c9d0d8 0%,#e4e6e8 50%,#b8a18a 100%)}
.support-panel{left:511px;top:553px;width:244px;height:163px;background:var(--burgundy)}
.support-title{left:535px;top:575px;font-size:23px;font-weight:700;font-family:"Roboto Condensed","Roboto",sans-serif;letter-spacing:.5px}
.support-copy{left:539px;top:608px;width:195px;font-size:7.5px;line-height:15.6px}

.btn{display:flex;align-items:center;justify-content:center;gap:6px;background:var(--gold);color:var(--white);font-size:7.5px;font-weight:700;letter-spacing:.2px}
.btn-support{left:540px;top:665px;width:113px;height:25px}

/* feature row */
.feature{top:716px;width:378px;height:273px}
.feature-industry{left:0;background:linear-gradient(170deg,#8d5b6a 0%,#9c4c4e 45%,#7b3a33 100%)}
.feature-world{left:378px;width:377px;background:linear-gradient(170deg,#9a6e86 0%,#a35a5a 45%,#7e3a36 100%)}
.feature-veil{left:0;top:0;width:100%;height:100%;background:rgba(120,30,35,.35)}
.feature-title{left:0;top:78px;width:100%;text-align:center;font-size:24px;font-weight:700;font-family:"Roboto Condensed","Roboto",sans-serif;letter-spacing:.3px}
.feature-copy{left:60px;top:121px;width:258px;text-align:center;font-size:7.5px;line-height:15.6px}
.feature-btn{left:136px;top:160px;width:106px;height:25px}

/* footer */
.site-footer{left:0;top:989px;width:755px;height:178px;background:var(--footer)}
.f-head{font-size:9.5px;font-weight:700;color:var(--gold-light);letter-spacing:.2px}
.f-text{font-size:7.3px;color:var(--footer-text);line-height:16.2px}
.f-list{list-style:none}
.newsletter-input{left:64px;top:1061px;width:183px;height:23px;background:var(--white);color:#777;font-size:7.3px;padding:7px 9px}
.btn-subscribe{left:64px;top:1093px;width:80px;height:22px}
.contact-name{color:var(--white)}
.contact-phone{display:flex;align-items:center;gap:5px}
.contact-phone b{font-weight:400;color:var(--gold-light)}
.footer-brand{left:565px;top:1118px;display:flex;align-items:center;gap:7px;font-size:14px;letter-spacing:1.5px;color:var(--gold-light)}
.footer-brand .brand-mark{width:11px;height:11px}

.legal-bar{left:0;top:1167px;width:755px;height:33px;background:var(--bar);display:flex;align-items:center;justify-content:center;gap:13px;font-size:7.3px;color:var(--footer-text)}
</style>
</head>
<body>

<header class="site-header abs">
  <div class="brand abs"><span class="brand-mark"></span>VELTRIX</div>
  <nav class="main-nav abs">
    <span>HOME</span><span>ABOUT US</span><span>SERVICES</span><span>TESTIMONIALS</span><span>CONTACT US</span>
  </nav>
</header>

<section class="hero abs" role="img" aria-label="Passenger jet flying above clouds at sunset">
  <div class="hero-photo abs"></div>
  <h1 class="hero-title abs">VELTRIX</h1>
  <p class="hero-tagline abs">OUR GOAL IS TO PROVIDE BOTH A SUPERIOR CUSTOMER<br>EXPERIENCE AND TREMENDOUS VALUE.</p>
  <div class="hero-dots abs"><i></i><i></i><i></i><i></i><i></i></div>
  <svg class="scroll-down abs" width="25" height="25" viewBox="0 0 25 25">
    <circle cx="12.5" cy="12.5" r="11.7" fill="none" stroke="#fff" stroke-width="1"/>
    <path d="M9 11l3.5 3.5L16 11" fill="none" stroke="#fff" stroke-width="1"/>
  </svg>
</section>

<div class="about-photo abs" role="img" aria-label="Private business jet parked on the apron"></div>
<section class="about-panel abs"></section>
<h2 class="about-kicker abs">ABOUT</h2>
<h2 class="about-title abs">VELTRIX</h2>
<div class="about-copy abs">
  <p>Lorem Ipsum is simply dummy text of the printing and typesetting industry. Lorem Ipsum has been the industry's standard dummy text ever since the 1500s, when an unknown printer took a galley of type and scrambled it to make a type specimen book.</p>
  <p>It has survived not only five centuries, but also the leap into electronic typesetting, remaining essentially unchanged. It was popularised in the 1960s with the release of Letraset sheets containing Lorem Ipsum passages...</p>
</div>

<div class="support-photo abs" role="img" aria-label="Support agents wearing headsets at a call centre"></div>
<section class="support-panel abs"></section>
<h2 class="support-title abs">AERIAL SUPPORT</h2>
<p class="support-copy abs">Lorem Ipsum is simply dummy text of the printing and typesetting industry. Lorem Ipsum has been the industry's standard dummy text...</p>
<div class="btn btn-support abs">EXPLORE OUR MENU
  <svg width="11" height="8" viewBox="0 0 11 8"><path d="M0 4h10M7 1l3 3-3 3" fill="none" stroke="#fff" stroke-width="1"/></svg></div>

<section class="feature feature-industry abs" role="img" aria-label="Helicopter on a landing pad">
  <div class="feature-veil abs"></div>
  <h2 class="feature-title abs">INDUSTRY LEADING</h2>
  <p class="feature-copy abs">Lorem Ipsum is simply dummy text of the printing and typesetting industry. Lorem Ipsum has been the industry</p>
  <div class="btn feature-btn abs">READ MORE INFO
    <svg width="11" height="8" viewBox="0 0 11 8"><path d="M0 4h10M7 1l3 3-3 3" fill="none" stroke="#fff" stroke-width="1"/></svg></div>
</section>

<section class="feature feature-world abs" role="img" aria-label="Traveller with luggage walking beside an airliner">
  <div class="feature-veil abs"></div>
  <h2 class="feature-title abs">WORLDWIDE PRESENCE</h2>
  <p class="feature-copy abs">Lorem Ipsum is simply dummy text of the printing and typesetting industry. Lorem Ipsum has been the industry</p>
  <div class="btn feature-btn abs">READ MORE INFO
    <svg width="11" height="8" viewBox="0 0 11 8"><path d="M0 4h10M7 1l3 3-3 3" fill="none" stroke="#fff" stroke-width="1"/></svg></div>
</section>

<footer class="site-footer abs"></footer>
<div class="abs" style="left:63px;top:1022px">
  <h3 class="f-head">NEWSLETTER SIGNUP</h3>
  <p class="f-text" style="margin-top:4px">Get our recent updates through your email id</p>
</div>
<div class="newsletter-input abs">Enter your email id</div>
<div class="btn btn-subscribe abs">SUBSCRIBE
  <svg width="11" height="8" viewBox="0 0 11 8"><path d="M0 4h10M7 1l3 3-3 3" fill="none" stroke="#fff" stroke-width="1"/></svg></div>

<div class="abs" style="left:311px;top:1022px">
  <h3 class="f-head">WELCOME</h3>
  <ul class="f-list f-text" style="margin-top:4px"><li>Home</li><li>About Us</li><li>Services</li><li>Testimonials</li><li>Contact Us</li></ul>
</div>
<div class="abs" style="left:429px;top:1022px">
  <h3 class="f-head">INFORMATION</h3>
  <ul class="f-list f-text" style="margin-top:4px"><li>Terms &amp; Conditions</li><li>Privacy Policy</li><li>Disclaimer</li><li>Sitemap</li></ul>
</div>
<div class="abs" style="left:563px;top:1022px">
  <h3 class="f-head">CONTACT INFO</h3>
  <div class="f-text" style="margin-top:4px;line-height:15px">
    <p class="contact-name">Veltrix</p>
    <p style="margin-top:2px">120 Street name, City name name,<br>Country name : 5666995</p>
    <p class="contact-phone" style="margin-top:3px">
      <svg width="7" height="7" viewBox="0 0 24 24"><path fill="#b8912e" d="M6.6 10.8a15 15 0 006.6 6.6l2.2-2.2c.3-.3.7-.4 1-.2 1.1.4 2.3.6 3.6.6.6 0 1 .4 1 1V20c0 .6-.4 1-1 1A17 17 0 013 4c0-.6.4-1 1-1h3.5c.6 0 1 .4 1 1 0 1.3.2 2.5.6 3.6.1.3 0 .7-.2 1z"/></svg>
      Phone: <b>555-014-2287</b></p>
  </div>
</div>
<div class="footer-brand abs"><span class="brand-mark"></span>VELTRIX</div>

<div class="legal-bar abs">
  <span>© 2016. Veltrix. All Rights Reserved.</span><span>Terms &amp; Conditions</span><span>Privacy Policy</span><span>Disclaimer</span>
</div>

</body>
</html>
```